Design for a Service-Based Estimate

We want a design for an Estimate that will always be sent in PDF format. The estimate or proposal is a critical document that needs to plainly show the service items, item description but also needs to be attractive and professional looking. Our current estimate deliverable is attached but it looks really basic like a Word document

```html
<!DOCTYPE html>
<html lang="en">
<head>
<meta charset="utf-8">
<title>Estimate</title>
<link rel="stylesheet" href="https://fonts.googleapis.com/css2?family=Archivo:wght@400;700;900&display=swap">
<style>
  :root {
    --backdrop: #c9c9c9;
    --paper: #ffffff;
    --ink: #111111;
    --ink-soft: #555555;
    --ink-muted: #8a8a8a;
    --heading-faint: #b4b4b4;
    --logo-grey: #cccccc;
    --band: #ececec;
    --bar: #e3e3e3;
  }
  * { box-sizing: border-box; margin: 0; padding: 0; }
  html, body {
    width: 1200px; height: 960px; overflow: hidden;
    background: var(--backdrop);
    font-family: "Archivo", Arial, sans-serif;
    color: var(--ink);
  }
  .page {
    position: absolute; left: 260px; top: 10px;
    width: 680px; height: 940px;
    background: var(--paper);
    padding: 186px 60px 0;
    display: flex; flex-direction: column;
  }
  .logo-slot {
    position: absolute; top: 70px; right: 64px;
    font-size: 34px; font-weight: 900; letter-spacing: 1px;
    color: var(--logo-grey);
  }
  .doc-title {
    font-size: 48px; line-height: 56px; font-weight: 900; color: var(--ink-soft);
    letter-spacing: -0.5px;
  }
  .section-heading {
    font-weight: 900; color: var(--heading-faint); letter-spacing: 0.5px;
  }
  .recipient { margin-top: 4px; }
  .recipient .section-heading { font-size: 20px; line-height: 24px; }
  .barred {
    border-left: 12px solid var(--bar);
    padding-left: 20px;
  }
  .recipient .barred { margin-top: 6px; padding-top: 2px; padding-bottom: 14px; }
  .recipient p { font-size: 16px; line-height: 22px; }
  .recipient .project { font-weight: 700; }

  .line-items {
    margin-top: 20px;
    width: 560px; border-collapse: collapse; font-size: 11.5px;
  }
  .line-items th {
    font-weight: 400; color: var(--ink-muted); font-size: 13px;
    text-align: left; padding: 0 8px 6px;
  }
  .line-items td { padding: 8px; vertical-align: top; line-height: 16px; color: #333; }
  .line-items .num { text-align: center; }
  .line-items .money { text-align: right; }
  .line-items tbody tr:first-child { background: var(--band); }
  .line-items .col-item { width: 300px; }
  .line-items .amount { font-weight: 700; color: var(--ink); }
  .line-items tfoot td { padding-top: 20px; font-size: 14px; font-weight: 700; color: var(--ink); }

  .terms { margin-top: 30px; width: 470px; }
  .terms .section-heading { font-size: 24px; line-height: 30px; }
  .terms .barred { margin-top: 8px; padding-bottom: 12px; }
  .terms p { font-size: 11.5px; line-height: 16px; color: #666; }

  .sign-off { margin-top: 22px; }
  .sign-off .section-heading { font-size: 22px; line-height: 34px; }
</style>
</head>
<body>
  <main class="page">
    <div class="logo-slot">LOGO</div>

    <h1 class="doc-title">ESTIMATE</h1>

    <section class="recipient">
      <h2 class="section-heading">RECIPIENT</h2>
      <div class="barred">
        <p class="project">Dana Whitcombe New Concrete Pad</p>
        <p>Dana Whitcombe</p>
        <p>48 Harbor Lane Millbrook 20415</p>
        <p>dwhitcombe@mailbox.test</p>
        <p>555 010 200</p>
      </div>
    </section>

    <table class="line-items">
      <thead>
        <tr>
          <th class="col-item">Item</th>
          <th class="num">Quantity</th>
          <th class="num">U/M</th>
          <th class="money">Unit $</th>
          <th class="money">Total $</th>
        </tr>
      </thead>
      <tbody>
        <tr>
          <td>Pour and finish four inch slab over compacted gravel base with forms, wire mesh, broom finish and control joints.</td>
          <td class="num">576</td>
          <td class="num">SF</td>
          <td class="money">$8.65</td>
          <td class="money amount">$4,982.40</td>
        </tr>
        <tr>
          <td>Thickened edge along the garage side for the new walkway.</td>
          <td class="num">48</td>
          <td class="num">SF</td>
          <td class="money">$8.65</td>
          <td class="money amount">$415.20</td>
        </tr>
      </tbody>
      <tfoot>
        <tr>
          <td colspan="4">Total Price</td>
          <td class="money">$5,397.60</td>
        </tr>
      </tfoot>
    </table>

    <section class="terms">
      <h2 class="section-heading">TERMS AND CONDITIONS</h2>
      <div class="barred">
        <p>This estimate is valid for thirty days from the date shown below. A deposit of fifty percent is due on acceptance, with the balance payable on completion. Prices assume clear site access and normal soil conditions; removal of rock, roots or old concrete is quoted separately. Pour dates depend on weather. Minor hairline cracking is natural to concrete and is not a defect. Changes to scope must be agreed in writing. Signing below confirms acceptance of these terms.</p>
      </div>
    </section>

    <section class="sign-off">
      <h2 class="section-heading">DATE</h2>
      <h2 class="section-heading">CLIENT SIGNATURE</h2>
    </section>
  </main>
</body>
</html>
```